Malvora Vitamins

I am reaching out to discuss a design project for a food supplement line for my company, Malvora Pharma GmBH. I am looking for a design that is colorful, creative, consistent, and indicative of each product. Initially, we have two items in our product range:
1. Folic Acid 400 with B12+B6 (Box)
2. Vitamin D3 50,000 IU (Label)
I have attached the source files from another company for each item, including the die cuts, so feel free to change the logo and address and come up with a new theme.
The new address is: Kolbergweg 42 .36211 Fulda, Germany

Target Market(s)

Middle East

Industry/Entity Type

Vitamins

Font styles to use
Sans Serif

Colors
0054AA
0677BA
7BADD7
CADEEF
E8F1F8
6B429C
8869AF
B7A5CE
E3DAEB
F3F0F8

Requirements
Must have
• Flores and photos to iditify the product

```html
<!DOCTYPE html>
<html lang="en">
<head>
<meta charset="utf-8">
<title>Malvora Folic Acid – Box Dieline</title>
<link rel="stylesheet" href="https://fonts.googleapis.com/css2?family=Roboto:ital,wght@0,400;0,500;0,700;0,900;1,700&display=swap">
<style>
  :root{
    --blue-deep:#0054AA;
    --blue:#0677BA;
    --blue-mid:#7BADD7;
    --blue-soft:#CADEEF;
    --blue-mist:#E8F1F8;
    --violet-deep:#6B429C;
    --violet:#8869AF;
    --violet-mid:#B7A5CE;
    --violet-soft:#E3DAEB;
    --violet-mist:#F3F0F8;
    --ink:#1d1d1d;
    --cut:#eea3b3;
    --fold:#8db4df;
    --dim:#222;
    --paper:#ffffff;
  }
  *{box-sizing:border-box;margin:0;padding:0}
  html,body{width:1198px;height:1200px;overflow:hidden;background:var(--paper)}
  body{font-family:"Roboto",Arial,sans-serif;color:var(--ink)}
  .stage{position:absolute;left:0;top:0;width:770px;height:771px;transform:scale(1.5558);transform-origin:0 0}
  .dieline{position:absolute;left:0;top:0;width:770px;height:771px;z-index:3;pointer-events:none}
  .dim-label{position:absolute;font-size:13px;color:var(--dim);font-weight:400}

  /* side panels */
  .side-left{position:absolute;left:110px;top:223px;width:63px;height:312px;background:linear-gradient(180deg,var(--violet-mist),var(--blue-mist))}
  .side-left .accent{position:absolute;left:0;top:0;width:63px;height:24px;background:var(--violet-deep)}
  .side-brand{position:absolute;left:22px;top:36px;font-size:13px;font-weight:700;color:var(--violet-deep);writing-mode:vertical-rl;letter-spacing:.5px}
  .side-right{position:absolute;left:370px;top:223px;width:66px;height:312px;background:linear-gradient(180deg,var(--violet-mist),var(--blue-mist))}
  .side-right .accent{position:absolute;left:0;top:0;width:66px;height:24px;background:var(--violet-deep)}

  /* front panel */
  .front{position:absolute;left:173px;top:223px;width:197px;height:312px;overflow:hidden;background:linear-gradient(180deg,#fff 0%,#fff 60%,var(--violet-mist) 100%)}
  .front-band{position:absolute;left:0;top:0;width:197px;height:24px;background:linear-gradient(90deg,var(--violet-deep),var(--violet));color:#fff;font-size:7px;font-weight:500;text-align:right;padding:8px 8px 0 0}
  .front-brand{position:absolute;left:10px;top:33px;display:flex;align-items:center;gap:5px;font-size:19px;font-weight:700;color:var(--violet-deep)}
  .front-brand .dot{width:8px;height:8px;border-radius:50%;background:var(--blue)}
  .front-photo{position:absolute;left:100px;top:24px;width:97px;height:200px;border-radius:97px 0 0 97px;background:radial-gradient(circle at 35% 40%,var(--violet-soft) 0%,var(--violet-mid) 45%,var(--blue-mid) 80%,var(--blue) 100%)}
  .product-name{position:absolute;left:10px;top:92px;font-size:27px;line-height:26px;font-weight:900;color:var(--violet-deep)}
  .dose-band{position:absolute;left:0;top:160px;width:132px;height:34px;background:linear-gradient(90deg,var(--blue-deep),var(--blue));clip-path:polygon(0 0,100% 0,88% 100%,0 100%);color:#fff;padding:5px 0 0 10px}
  .dose-band .dose{font-size:12px;font-weight:700;font-style:italic;line-height:13px}
  .dose-band .with{font-size:6.4px;font-weight:500;line-height:9px}
  .claims{position:absolute;left:10px;top:206px;list-style:none}
  .claims li{font-size:6.2px;font-weight:500;line-height:13px;padding-left:11px;position:relative;color:var(--ink)}
  .claims svg{position:absolute;left:0;top:3.5px;width:7px;height:7px}
  .origin{position:absolute;left:10px;top:276px;display:flex;align-items:center;gap:5px;font-size:6.4px;font-weight:500}
  .count-box{position:absolute;left:107px;top:255px;width:90px;height:57px;background:linear-gradient(135deg,var(--violet-deep),var(--violet));color:#fff;padding:17px 0 0 10px;border-top-left-radius:14px}
  .count-box .count{font-size:10.5px;font-weight:700;line-height:12px}
  .count-box .weight{font-size:6.2px;line-height:10px}

  /* back panel */
  .back{position:absolute;left:440px;top:228px;width:190px;font-size:5.1px;line-height:6.3px}
  .back p{margin-bottom:5px}
  .back h3{font-size:5.3px;font-weight:700;margin-bottom:1px;color:var(--violet-deep)}
  .back ul{list-style:none}
  .back strong{font-weight:700;color:var(--violet-deep)}
  .facts{width:130px;margin:2px 0 0 31px;border-collapse:collapse;font-size:4.2px;line-height:5.3px}
  .facts th.head{background:var(--violet-deep);color:#fff;font-size:5px;padding:1px 0}
  .facts th{font-weight:700;text-align:center;border:.3px solid var(--violet-mid);padding:0 2px}
  .facts td{border:.3px solid var(--violet-mid);padding:0 2px;text-align:center}
  .facts td:first-child{text-align:left}
  .facts tr:nth-child(even) td{background:var(--violet-mist)}
  .footnote{font-size:2.8px;margin:2px 0 0 31px}
  .maker{position:absolute;left:500px;top:506px;width:128px;text-align:right;font-size:4.6px;line-height:7px}
  .maker strong{color:var(--violet-deep)}
  .batch{position:absolute;left:455px;top:544px;font-size:5.5px;line-height:14.5px}
</style>
</head>
<body>
<div class="stage">
  <div class="side-left"><div class="accent"></div><div class="side-brand">Malvora</div></div>
  <div class="side-right"><div class="accent"></div></div>

  <section class="front">
    <div class="front-band">Dietary Supplement</div>
    <div class="front-photo" role="img" aria-label="Photo of fresh spinach leaves with violet flowers"></div>
    <div class="front-brand"><span class="dot"></span>Malvora</div>
    <h1 class="product-name">Folic<br>Acid</h1>
    <div class="dose-band">
      <div class="dose">400 µg</div>
      <div class="with">with VITAMIN B12 &amp; B6</div>
    </div>
    <ul class="claims">
      <li><svg viewBox="0 0 8 8" aria-hidden="true"><circle cx="4" cy="4" r="4" fill="var(--violet)"/><path d="M2 4.2 3.4 5.5 6 2.7" fill="none" stroke="#fff" stroke-width="1"/></svg>Made to High Standards of Quality Control</li>
      <li><svg viewBox="0 0 8 8" aria-hidden="true"><circle cx="4" cy="4" r="4" fill="var(--violet)"/><path d="M2 4.2 3.4 5.5 6 2.7" fill="none" stroke="#fff" stroke-width="1"/></svg>No Artificial Colours or Preservatives</li>
      <li><svg viewBox="0 0 8 8" aria-hidden="true"><circle cx="4" cy="4" r="4" fill="var(--violet)"/><path d="M2 4.2 3.4 5.5 6 2.7" fill="none" stroke="#fff" stroke-width="1"/></svg>Suitable for Vegans</li>
    </ul>
    <div class="origin">
      <svg width="18" height="18" viewBox="0 0 18 18" aria-hidden="true">
        <clipPath id="flag"><circle cx="9" cy="9" r="9"/></clipPath>
        <g clip-path="url(#flag)"><rect width="18" height="6" fill="#000"/><rect y="6" width="18" height="6" fill="#dd0000"/><rect y="12" width="18" height="6" fill="#ffce00"/></g>
      </svg>
      Made in Germany
    </div>
    <div class="count-box">
      <div class="count">30 Tablets</div>
      <div class="weight">Net weight: 3.6 g ℮</div>
    </div>
  </section>

  <section class="back">
    <p><strong>Folic Acid</strong> is a food supplement rich in folic acid and vitamins B6 &amp; B12. Folate, Vitamins B6 and B12 contribute to normal homocysteine metabolism and red blood cells formation.</p>
    <h3>Ingredients</h3>
    <p>Starch; Maltodextrin; Bulking Agents: Lactose Monohydrate (contains Milk), Microcrystalline Cellulose; Cyanocobalamin (Vitamin B12); Pyridoxine hydrochloride (Vitamin B6); Anti-Caking Agent: Magnesium Salts of Fatty Acids; Pteroylmonoglutamic Acid (Folic Acid).</p>
    <h3>Directions for use</h3>
    <p>For adults, take one tablet daily with sufficient amount of water.</p>
    <h3>Precautions</h3>
    <ul>
      <li>• Keep out of reach of children.</li>
      <li>• The recommended daily intake indicated may not be exceeded.</li>
      <li>• Do not use after the expiry date printed on the box.</li>
    </ul>
    <p><strong>Disclaimer:</strong> Food supplements are not a substitute for a varied, balanced diet and a healthy way of living.</p>
    <h3>Storage Conditions</h3>
    <ul style="margin-bottom:5px">
      <li>• Store in the original package, in a cool (&lt; 25°C) and dry place.</li>
      <li>• Protect the product from light and moisture.</li>
    </ul>
    <table class="facts">
      <tr><th class="head" colspan="3">Nutritional Information</th></tr>
      <tr><th>Nutritional Values</th><th>Per Tablet</th><th>Per 100 g</th></tr>
      <tr><td>Energy</td><td>2 kJ / 0 kcal</td><td>1491 kJ / 356 kcal</td></tr>
      <tr><td>Fat</td><td>&lt; 0.1 g</td><td>0.5 g</td></tr>
      <tr><td>of which saturates</td><td>&lt; 0.1 g</td><td>0.3 g</td></tr>
      <tr><td>Carbohydrate</td><td>&lt; 0.1 g</td><td>86.3 g</td></tr>
      <tr><td>of which sugars</td><td>&lt; 0.1 g</td><td>20.0 g</td></tr>
      <tr><td>Protein</td><td>&lt; 0.1 g</td><td>&lt; 0.1 g</td></tr>
      <tr><td>Salt</td><td>&lt; 0.01 g</td><td>0.05 g</td></tr>
      <tr><th class="head" colspan="3">Composition</th></tr>
      <tr><th>Ingredients</th><th>Per Tablet</th><th>%NRV*</th></tr>
      <tr><td>Vitamin B6</td><td>1.9 mg</td><td>136</td></tr>
      <tr><td>Folic Acid</td><td>400 µg</td><td>200</td></tr>
      <tr><td>Vitamin B12</td><td>2.5 µg</td><td>100</td></tr>
    </table>
    <div class="footnote">*NRV: Nutrient Reference Values according to Regulation (EU) No 1169/2011</div>
  </section>

  <div class="maker"><strong>Made in Germany By:</strong> Malvora Pharma GmBH<br>Kolbergweg 42 .36211 Fulda, Germany</div>
  <div class="batch">Batch No.:<br>Mfg. Date:<br>Exp. Date:</div>

  <svg class="dieline" viewBox="0 0 770 771" aria-hidden="true">
    <g fill="none" stroke="var(--cut)" stroke-width="0.8">
      <path d="M110 223 H173 V190 H180 V162 Q180 150 192 150 H351 Q363 150 363 162 V190 H370 V223 H436 V205 H633 V223 L673 235 V523 L633 535 V540 Q633 545 628 548 L615 600 H610 V640 H460 V600 H455 L441 548 Q436 545 436 540 V535 H370 V580 H173 V535 H110 Z"/>
      <path d="M110 223 L114 203 Q117 195 125 195 H160 L173 210"/>
      <path d="M370 223 L376 203 Q379 195 387 195 H424 L436 210"/>
      <path d="M110 535 L114 560 Q117 578 128 578 H160 L173 550"/>
      <path d="M370 535 L376 560 Q379 578 390 578 H424 L436 550"/>
      <path d="M173 570 L180 580 M370 570 L363 580"/>
    </g>
    <g fill="none" stroke="var(--fold)" stroke-width="0.7">
      <path d="M173 223 V535 M370 223 V535 M436 223 V535 M633 223 V535"/>
      <path d="M110 223 H633 M110 535 H633 M180 190 H363 M460 600 H610"/>
    </g>
    <g fill="none" stroke="var(--dim)" stroke-width="0.6">
      <path d="M70 150 V535 M65 150 H110 M65 223 H110 M65 535 H110 M65 580 H110"/>
      <path d="M70 535 V580"/>
      <path d="M720 223 V640 M633 223 H725 M633 535 H725 M633 600 H725 M633 640 H725"/>
      <path d="M97 657 H673 M97 652 V662 M173 590 V662 M370 590 V662 M436 650 V662 M633 650 V662 M673 650 V662"/>
    </g>
    <g fill="var(--dim)">
      <path d="M70 150 l-2 5 h4z M70 223 l-2 -5 h4z M70 223 l-2 5 h4z M70 535 l-2 -5 h4z M70 535 l-2 5 h4z M70 580 l-2 -5 h4z"/>
      <path d="M720 223 l-2 5 h4z M720 535 l-2 -5 h4z M720 535 l-2 5 h4z M720 600 l-2 -5 h4z M720 600 l-2 5 h4z M720 640 l-2 -5 h4z"/>
      <path d="M97 657 l5 -2 v4z M173 657 l-5 -2 v4z M173 657 l5 -2 v4z M370 657 l-5 -2 v4z M370 657 l5 -2 v4z M436 657 l-5 -2 v4z M436 657 l5 -2 v4z M633 657 l-5 -2 v4z M633 657 l5 -2 v4z M673 657 l-5 -2 v4z"/>
    </g>
  </svg>

  <span class="dim-label" style="left:55px;top:193px">18.5</span>
  <span class="dim-label" style="left:57px;top:371px">122</span>
  <span class="dim-label" style="left:55px;top:541px">18.5</span>
  <span class="dim-label" style="left:690px;top:371px">122.5</span>
  <span class="dim-label" style="left:690px;top:558px">24.5</span>
  <span class="dim-label" style="left:697px;top:603px">12</span>
  <span class="dim-label" style="left:108px;top:662px">25.25</span>
  <span class="dim-label" style="left:263px;top:662px">77</span>
  <span class="dim-label" style="left:395px;top:662px">26</span>
  <span class="dim-label" style="left:526px;top:662px">77</span>
  <span class="dim-label" style="left:643px;top:662px">15</span>
</div>
</body>
</html>
```